Steady Valve Systems

I need a business card with the attached logo.
The second page I have attached is what we are looking for. We want doubles sided. We would like the blues fading and the logo on the back.

Industry/Entity Type

Business

```html
<!DOCTYPE html>
<html lang="en">
<head>
<meta charset="utf-8">
<title>Steady Valve Systems – Business Card</title>
<link href="https://fonts.googleapis.com/css2?family=Open+Sans:ital,wght@0,400;0,600;0,700;1,400&display=swap" rel="stylesheet">
<style>
  :root {
    --stage: #d9dadc;
    --card: #ffffff;
    --brand-blue: #1b3d96;
    --blue-deep: #0c2670;
    --blue-bright: #2a55b8;
    --stripe-grey: #a9abb0;
    --stripe-light: #d6d7da;
    --ink: #2b2d33;
    --on-blue: #ffffff;
  }
  * { margin: 0; padding: 0; box-sizing: border-box; }
  html, body { width: 1200px; height: 772px; overflow: hidden; }
  body {
    background: var(--stage);
    font-family: "Open Sans", Arial, sans-serif;
    display: flex;
    align-items: center;
    justify-content: center;
    gap: 40px;
  }
  .card {
    position: relative;
    width: 540px;
    height: 309px;
    background: var(--card);
    box-shadow: 0 6px 18px rgba(0,0,0,0.18);
    overflow: hidden;
  }
  .wordmark {
    color: var(--brand-blue);
    font-weight: 700;
    letter-spacing: 0.04em;
    text-transform: uppercase;
    white-space: nowrap;
  }
  /* back side */
  .card-back .wordmark {
    position: absolute;
    left: 40px;
    top: 130px;
    font-size: 33px;
  }
  /* front side */
  .card-front .wave { position: absolute; inset: 0; }
  .card-front .wordmark {
    position: absolute;
    right: 36px;
    top: 34px;
    font-size: 22px;
  }
  .holder {
    position: absolute;
    left: 34px;
    top: 82px;
    color: var(--ink);
  }
  .holder-name { font-weight: 700; font-size: 15px; }
  .holder-role { font-style: italic; font-size: 13px; }
  .contact {
    position: absolute;
    right: 30px;
    bottom: 24px;
    list-style: none;
    text-align: right;
    color: var(--on-blue);
    font-size: 11px;
    line-height: 1.6;
  }
  .contact li { display: flex; justify-content: flex-end; align-items: center; gap: 6px; }
  .contact svg { width: 10px; height: 10px; fill: var(--on-blue); }
</style>
</head>
<body>

  <section class="card card-back" aria-label="Card back">
    <div class="wordmark">Steady Valve Systems</div>
  </section>

  <section class="card card-front" aria-label="Card front">
    <svg class="wave" viewBox="0 0 540 309" preserveAspectRatio="none" aria-hidden="true">
      <defs>
        <linearGradient id="blueFade" x1="0" y1="0" x2="1" y2="1">
          <stop offset="0" stop-color="var(--blue-bright)"/>
          <stop offset="1" stop-color="var(--blue-deep)"/>
        </linearGradient>
      </defs>
      <path d="M0,118 C170,100 300,200 540,138 L540,309 L0,309 Z" fill="var(--stripe-light)"/>
      <path d="M0,128 C170,112 300,212 540,152 L540,309 L0,309 Z" fill="var(--stripe-grey)"/>
      <path d="M0,142 C170,128 300,228 540,168 L540,309 L0,309 Z" fill="url(#blueFade)"/>
    </svg>

    <div class="wordmark">Steady Valve Systems</div>

    <div class="holder">
      <p class="holder-name">Darren Kell-Moore</p>
      <p class="holder-role">Consultant</p>
    </div>

    <ul class="contact">
      <li>27 Harbour Point,</li>
      <li>Kestrel Road NTB</li>
      <li>012 555 0142
        <svg viewBox="0 0 10 10" aria-hidden="true"><path d="M2 0.5 L3.6 2.6 L2.8 3.6 C3.4 5 4.6 6.3 6.2 7 L7.2 6.2 L9.5 7.6 L8.6 9.5 C4.5 9.2 0.8 5.4 0.5 1.4 Z"/></svg>
      </li>
      <li>012 555 0143
        <svg viewBox="0 0 10 10" aria-hidden="true"><rect x="1" y="2" width="8" height="7" rx="1"/></svg>
      </li>
      <li>info@steadyvalve.co
        <svg viewBox="0 0 10 10" aria-hidden="true"><path d="M0.5 2 H9.5 V8.5 H0.5 Z M0.5 2 L5 5.5 L9.5 2" stroke="#fff" stroke-width="0.6" fill="none"/></svg>
      </li>
      <li>www.steadyvalve.co</li>
    </ul>
  </section>

</body>
</html>
```